依頼詳細
<取扱商品>
レディースバレエシューズ・ルームシューズ・除菌スプレー・マスクケースなど

<ターゲット>
やや女性向け
基本は老若男女問わず

<使用画像について>
商品画像はコンペ終了後にお渡ししますので仮の画像を入れていただければと思います。
商品画像以外の使用素材は有料のものでも問題は有りませんが、quilva picsまたは低価格(0~2000円程度)のものでお願いします。
※もし有料素材を使う場合は最初から購入して頂く必要はないのでウォーターマーク付きのもので提案していただければ大丈夫です。

<デザイン>
明るめのやさしい感じでお願いします。
参考サイトほどピンクは強めでなくてもいいかと思いますが、デザイン次第では濃い色の使用もありかと思います。

参考サイト
https://pelrovin.jp/

<ページ幅>
1920pxでお願いします。

<特筆事項>
今回NIVOを使用するにあたりプラン的にNIVOマークが必須になります。
右上のテントのマークはありきでお願いします。

今後も定期的にデザインをお願いすることができる技量を持つ方を探しておりますので是非、単発と考えずにデザインを出していただければと思います。
それでは皆様のご応募よろしくお願い致します。
サイトURL
ページ数
1ページ
希望イメージ
シンプル 複雑
単色 カラフル
暗い 明るい
日常 高級
遊び心 厳粛
未来的 伝統的
女性的 男性的
希望する色
白・淡いピンク・淡い水色などの優しい色
納品ファイル
• フォトショップ形式 (.psd)
補足説明
■ 選んだ理由

こちらが想定した以上のデザインでした。

■ 提案者全員のお礼・コメント

この度は当方コンペにご提案いただきありがとうございました。
提案頂いた方々のデザインはどれも素敵なもので、真剣に吟味し当選者を選択させていただきました。
今後もミルトカを利用してのデザインコンペを行う予定ですので、残念ながら今回は当選とならなかった方もまたご参加いただけると幸いです。
今後もどうかよろしくお願い致します。

```html
<!DOCTYPE html>
<html lang="ja">
<head>
<meta charset="utf-8">
<title>norumi</title>
<link rel="stylesheet" href="https://fonts.googleapis.com/css2?family=Noto+Sans+JP:wght@400;700;900&family=Montserrat:wght@700;800&display=swap">
<style>
:root{
  --sky:#d9eef8;
  --white:#ffffff;
  --ink:#1f1f1f;
  --band:#2b2b2b;
  --photo-a:#f4f4f4;
  --photo-b:#dcdcdc;
}
*{box-sizing:border-box;margin:0;padding:0}
html,body{width:1200px;height:3228px;overflow:hidden}
body{background:var(--sky);font-family:"Noto Sans JP",sans-serif;color:var(--ink);position:relative}
.site-header{position:absolute;left:0;top:0;width:1200px;height:88px;background:var(--white);display:flex;align-items:center;padding:0 0 0 112px}
.brand{font-family:"Montserrat",sans-serif;font-weight:800;font-size:36px;letter-spacing:1px}
.main-nav{display:flex;gap:44px;margin-left:120px;font-size:16px;font-weight:700}
.header-marks{position:absolute;right:40px;top:10px;display:flex;gap:12px}
.header-marks span{width:72px;height:68px;background:var(--white);border:1px solid #e3e3e3;display:block}
.hero{position:absolute;left:0;top:88px;width:1200px;height:672px;overflow:hidden;background:var(--sky)}
.photo-circle{position:absolute;border-radius:50%;background:radial-gradient(circle,var(--photo-a) 55%,var(--photo-b))}
.hero-card{position:absolute;left:400px;top:224px;width:400px;height:228px;background:var(--white);border:6px solid var(--ink);text-align:center;padding-top:40px}
.hero-card h1{font-family:"Montserrat",sans-serif;font-weight:800;font-size:52px}
.hero-card h2{font-size:15px;font-weight:700;margin-top:14px}
.hero-card p{font-size:12px;margin-top:12px}
.hero-rule{position:absolute;left:0;top:752px;width:1200px;height:8px;background:var(--ink)}
.hero-rule-thin{position:absolute;left:0;top:776px;width:1200px;height:2px;background:var(--white)}
.sdgs{position:absolute;left:168px;top:872px;width:864px;height:296px}
.bracket{position:absolute;top:0;width:44px;height:296px;border:10px solid var(--ink)}
.bracket.left{left:0;border-right:none}
.bracket.right{right:0;border-left:none}
.sdgs-dot{position:absolute;left:402px;top:36px;width:60px;height:60px;border-radius:50%;background:var(--ink)}
.sdgs h3{position:absolute;top:124px;width:100%;text-align:center;font-size:15px;font-weight:700}
.sdgs ul{position:absolute;top:160px;width:100%;list-style:none;text-align:center;font-size:12px;line-height:18px}
.section-head{position:absolute;left:0;top:1316px;width:1200px;text-align:center}
.section-head .bar{width:120px;height:10px;background:var(--ink);margin:0 auto 56px}
.section-head h2{font-family:"Montserrat",sans-serif;font-weight:800;font-size:54px;line-height:1}
.section-head p{font-size:15px;font-weight:700;margin-top:8px}
.product-card{position:absolute;width:508px;height:452px;background:var(--white);border:4px solid var(--band)}
.product-card header{height:76px;background:var(--band);color:var(--white);display:flex;align-items:center;padding-left:56px;font-size:22px;font-weight:700;gap:16px}
.product-card header svg{width:34px;height:20px}
.product-photo{position:absolute;left:0;top:76px;right:0;bottom:0}
.more-btn{position:absolute;left:488px;top:2540px;width:224px;height:60px;background:var(--band);color:var(--white);display:flex;align-items:center;justify-content:center;gap:14px;font-size:15px;font-weight:700}
.footer-rule{position:absolute;left:0;top:2728px;width:1200px;height:10px;background:var(--ink)}
.footer-links{position:absolute;top:2824px;left:0;width:1200px}
.footer-link{position:absolute;width:200px;text-align:center;font-size:16px;font-weight:700}
.footer-link svg{display:block;margin:0 auto 18px}
.legal{position:absolute;top:3044px;left:312px;width:576px;display:flex;justify-content:center;font-size:14px}
.legal span{padding:6px 36px;border-left:2px solid var(--ink);border-right:2px solid var(--ink)}
.legal span+span{border-left:none}
.copyright{position:absolute;top:3128px;width:1200px;text-align:center;font-size:17px;font-weight:700}
</style>
</head>
<body>
<header class="site-header">
  <div class="brand">norumi</div>
  <nav class="main-nav"><span>会社概要</span><span>商品一覧</span><span>よくあるご質問</span><span>お問い合わせ</span></nav>
  <div class="header-marks"><span></span><span></span></div>
</header>

<section class="hero">
  <div class="photo-circle" role="img" aria-label="赤いスニーカーの写真" style="left:100px;top:10px;width:280px;height:280px"></div>
  <div class="photo-circle" role="img" aria-label="黄色いパンプスの写真" style="left:650px;top:0;width:160px;height:160px"></div>
  <div class="photo-circle" role="img" aria-label="ベージュのスニーカーの写真" style="left:860px;top:120px;width:420px;height:420px"></div>
  <div class="photo-circle" role="img" aria-label="茶色の革靴の写真" style="left:-20px;top:360px;width:320px;height:320px"></div>
  <div class="photo-circle" role="img" aria-label="白いヒールの写真" style="left:500px;top:520px;width:140px;height:160px"></div>
  <div class="photo-circle" role="img" aria-label="靴の写真" style="left:600px;top:620px;width:150px;height:150px"></div>
  <div class="hero-card">
    <h1>norumi</h1>
    <h2>サスティナビリティ</h2>
    <p>わたしたちは自然環境に配慮した企業です。</p>
  </div>
</section>
<div class="hero-rule"></div>

<section class="sdgs">
  <div class="bracket left"></div><div class="bracket right"></div>
  <div class="sdgs-dot"></div>
  <h3>SDGsへの取り組み</h3>
  <ul>
    <li>素材選びから配送まで、環境への負担を減らす工夫を重ねています。</li>
    <li>長く使える品質を大切にし、修理や再利用の仕組みづくりを進めます。</li>
    <li>包装資材は再生紙を中心に、必要最小限の量でお届けしています。</li>
    <li>地域の工房と協力し、働く人にやさしいものづくりを続けています。</li>
    <li>これからも暮らしと地球の両方に寄り添う商品をご提案します。</li>
  </ul>
</section>

<div class="section-head">
  <div class="bar"></div>
  <h2>PRODUCT</h2>
  <p>商品一覧</p>
</div>

<article class="product-card" style="left:80px;top:1528px">
  <header><svg viewBox="0 0 34 20"><path d="M2 2l8 8-8 8M16 2l8 8-8 8" fill="none" stroke="#fff" stroke-width="4"/></svg>バレエシューズ</header>
  <div class="product-photo" role="img" aria-label="緑のバレエシューズの写真" style="background:radial-gradient(circle,#9fdad3 0 28%,#fff 62%)"></div>
</article>
<article class="product-card" style="left:612px;top:1528px">
  <header><svg viewBox="0 0 34 20"><path d="M2 2l8 8-8 8M16 2l8 8-8 8" fill="none" stroke="#fff" stroke-width="4"/></svg>ルームシューズ</header>
  <div class="product-photo" role="img" aria-label="紺色のルームシューズの写真" style="background:radial-gradient(circle,#3b4566 0 26%,#fff 62%)"></div>
</article>
<article class="product-card" style="left:80px;top:2012px">
  <header><svg viewBox="0 0 34 20"><path d="M2 2l8 8-8 8M16 2l8 8-8 8" fill="none" stroke="#fff" stroke-width="4"/></svg>抗ウイルス除菌スプレー</header>
  <div class="product-photo" role="img" aria-label="白いスプレーボトルの写真" style="background:radial-gradient(circle,#e6e6e6 0 30%,#fff 62%)"></div>
</article>
<article class="product-card" style="left:612px;top:2012px">
  <header><svg viewBox="0 0 34 20"><path d="M2 2l8 8-8 8M16 2l8 8-8 8" fill="none" stroke="#fff" stroke-width="4"/></svg>マスクケース</header>
  <div class="product-photo" role="img" aria-label="白いマスクの写真" style="background:radial-gradient(circle,#ececec 0 30%,#fff 62%)"></div>
</article>

<a class="more-btn">商品一覧へ<svg width="22" height="22" viewBox="0 0 22 22"><circle cx="11" cy="11" r="10" fill="#fff"/><path d="M8 6l5 5-5 5" fill="none" stroke="#2b2b2b" stroke-width="3"/></svg></a>

<div class="footer-rule"></div>
<footer>
  <div class="footer-links">
    <div class="footer-link" style="left:160px">
      <svg width="96" height="120" viewBox="0 0 96 120" fill="none" stroke="#1f1f1f" stroke-width="3"><rect x="12" y="30" width="34" height="84"/><rect x="46" y="50" width="34" height="64"/><path d="M20 20h20v10M4 114h88"/><path d="M20 42h6M32 42h6M20 56h6M32 56h6M20 70h6M32 70h6M54 62h6M66 62h6M54 76h6M66 76h6"/></svg>会社概要
    </div>
    <div class="footer-link" style="left:512px">
      <svg width="96" height="120" viewBox="0 0 96 120" fill="none" stroke="#1f1f1f" stroke-width="3"><rect x="10" y="36" width="62" height="44"/><path d="M10 36l31 26 31-26"/><circle cx="68" cy="84" r="20" fill="#d9eef8"/><path d="M60 76c0 10 6 16 16 16l3-5-5-3-3 3c-3-1-5-3-6-6l3-3-3-5z" fill="#1f1f1f" stroke="none"/></svg>お問い合わせ
    </div>
    <div class="footer-link" style="left:848px">
      <svg width="96" height="120" viewBox="0 0 96 120"><path d="M14 30a20 20 0 1 1 14 28l-10 6 2-10a20 20 0 0 1-6-24z" fill="#1f1f1f"/><text x="34" y="50" fill="#fff" font-family="Montserrat,sans-serif" font-size="18" font-weight="800" text-anchor="middle">Q</text><path d="M82 64a20 20 0 1 0-14 28l10 6-2-10a20 20 0 0 0 6-24z" fill="#1f1f1f"/><text x="62" y="84" fill="#fff" font-family="Montserrat,sans-serif" font-size="18" font-weight="800" text-anchor="middle">A</text></svg>よくある質問
    </div>
  </div>
  <div class="legal"><span>特定商取引法に基づく表記</span><span>プライバシーポリシー</span></div>
  <p class="copyright">@2020 norumi</p>
</footer>
</body>
</html>
```